Larkmoor Stationery Design Project

company name : Larkmoor General Trading LLC.
light watermark taken from the logo to cover almost the middle of the stationary..
logo is attached and an on going business card project is released on the same company name..
thanks
Reason: more time for more designs and to work with comfort..
Industry/Entity Type
Business
Colors
Designer to choose colors to be used in the design.
Look and feel
Each slider illustrates characteristics of the customer's brand and the style your logo design should communicate.

```html
<!DOCTYPE html>
<html lang="en">
<head>
<meta charset="utf-8">
<title>Larkmoor Int. Letterhead</title>
<link rel="stylesheet" href="https://fonts.googleapis.com/css2?family=Arimo:wght@400;700&family=Pinyon+Script&display=swap">
<style>
  :root {
    --ink: #2b2b2b;
    --ink-soft: #3a3a3a;
    --brand-grey: #4a4a4a;
    --brand-blue: #1e9bd7;
    --paper: #ffffff;
    --mist-grey: #e6e6e6;
    --mist-blue: #dcecf5;
  }
  html, body { margin: 0; padding: 0; overflow: hidden; background: var(--paper); }
  .letterhead {
    position: relative;
    width: 928px;
    height: 1200px;
    overflow: hidden;
    background: var(--paper);
    font-family: "Arimo", Arial, sans-serif;
    color: var(--ink);
  }
  .contact-block {
    position: absolute;
    left: 50px;
    top: 31px;
    font-size: 9.5px;
    line-height: 11.5px;
    color: var(--ink-soft);
  }
  .contact-item { display: flex; align-items: flex-start; margin-bottom: 5px; }
  .contact-item svg { width: 11px; height: 11px; margin-right: 3px; flex: none; fill: var(--brand-blue); }
  .brand-name {
    position: absolute;
    right: 34px;
    top: 92px;
    font-weight: 700;
    font-size: 28px;
    letter-spacing: 1px;
    color: var(--brand-grey);
    text-transform: uppercase;
  }
  .brand-dot {
    position: absolute;
    right: 40px;
    top: 40px;
    width: 38px;
    height: 38px;
    border-radius: 50%;
    background: var(--brand-blue);
  }
  .watermark {
    position: absolute;
    left: 48px;
    top: 812px;
    width: 860px;
    height: 370px;
  }
  .salutation {
    position: absolute;
    left: 76px;
    top: 235px;
    margin: 0;
    font-size: 17px;
  }
  .letter-body {
    position: absolute;
    left: 156px;
    top: 271px;
    width: 700px;
    font-size: 16.2px;
    line-height: 20.5px;
  }
  .letter-body p { margin: 0 0 20px; }
  .letter-body p.tight { margin-bottom: 0; }
  .sign-off {
    position: absolute;
    left: 106px;
    top: 850px;
    font-size: 16.5px;
    line-height: 20.5px;
  }
  .signature {
    position: absolute;
    left: 78px;
    top: 915px;
    font-family: "Pinyon Script", cursive;
    font-size: 50px;
    line-height: 1;
    color: var(--ink);
  }
  .signatory-role {
    position: absolute;
    left: 106px;
    top: 978px;
    font-size: 16.5px;
  }
</style>
</head>
<body>
<div class="letterhead">
  <svg class="watermark" role="img" aria-label="Faint brand wave watermark across the lower page" viewBox="0 0 860 370">
    <defs>
      <linearGradient id="mistGrey" x1="0" y1="1" x2="1" y2="0">
        <stop offset="0" stop-color="var(--mist-grey)" stop-opacity="0"/>
        <stop offset="0.5" stop-color="var(--mist-grey)" stop-opacity="0.7"/>
        <stop offset="1" stop-color="var(--mist-grey)" stop-opacity="0.2"/>
      </linearGradient>
      <linearGradient id="mistBlue" x1="0" y1="1" x2="1" y2="0">
        <stop offset="0" stop-color="var(--mist-blue)" stop-opacity="0.1"/>
        <stop offset="1" stop-color="var(--mist-blue)" stop-opacity="0.6"/>
      </linearGradient>
    </defs>
    <rect x="0" y="0" width="860" height="370" rx="180" fill="url(#mistGrey)" opacity="0.55"/>
    <rect x="380" y="120" width="460" height="250" rx="120" fill="url(#mistBlue)" opacity="0.6"/>
  </svg>

  <div class="contact-block">
    <div class="contact-item">
      <svg viewBox="0 0 12 12"><path d="M6 0a4 4 0 0 0-4 4c0 3 4 8 4 8s4-5 4-8a4 4 0 0 0-4-4zm0 5.5A1.5 1.5 0 1 1 6 2.5a1.5 1.5 0 0 1 0 3z"/></svg>
      <span>218 Harbor Lane East<br>Millbrook, ST&nbsp; 60412</span>
    </div>
    <div class="contact-item">
      <svg viewBox="0 0 12 12"><path d="M2.5 0.5l2 2.2-1 1.5c.8 1.7 2.2 3.1 3.9 3.9l1.5-1 2.1 2-1.2 2.3C4.9 11 1 7.1.3 2z"/></svg>
      <span>555-012-3456</span>
    </div>
    <div class="contact-item">
      <svg viewBox="0 0 12 12"><rect x="0.5" y="2" width="11" height="8"/></svg>
      <span>info@larkmoorint.com</span>
    </div>
    <div class="contact-item">
      <svg viewBox="0 0 12 12"><circle cx="6" cy="6" r="5.2" fill="none" stroke="var(--brand-blue)" stroke-width="1.2"/><ellipse cx="6" cy="6" rx="2.2" ry="5.2" fill="none" stroke="var(--brand-blue)" stroke-width="1"/><path d="M1 6h10" stroke="var(--brand-blue)" stroke-width="1"/></svg>
      <span>www.larkmoorint.com</span>
    </div>
  </div>

  <div class="brand-dot"></div>
  <div class="brand-name">Larkmoor Int.</div>

  <p class="salutation">Dear Sir / Madam,</p>

  <div class="letter-body">
    <p>Lorem ipsum dolor sit amet, consectetur adipisicing elit, sed do eiusmod tempor incididunt ut labore et dolore magna aliqua. Ut enim ad minim veniam, quis nostrud exercitation ullamco laboris nisi ut aliquip ex ea commodo consequa.Lorem ipsum dolor sit amet, consectetur adipisicing elit, sed do eiusmod tempor incididunt ut labore et dolore magna aliqua. Ut enim ad minim veniam, quis.</p>
    <p>Lorem ipsum dolor sit amet, consectetur adipisicing elit, sed do eiusmod tempor incididunt ut labore et dolore magna aliqua. Ut enim ad minim veniam, quis nostrud exercitation ullamco laboris nisi ut aliquip ex ea commodo consequa.Lorem ipsum dolor sit amet, consectetur adipisicing elit, sed do eiusmod tempor incididunt ut labore et dolore magna aliqua. Ut enim ad minim veniam, quis.</p>
    <p>Lorem ipsum dolor sit amet, consectetur adipisicing elit, sed do eiusmod tempor incididunt ut labore et dolore magna aliqua. Ut enim ad minim veniam, quis nostrud exercitation ullamco laboris nisi ut aliquip ex ea commodo consequa.Lorem ipsum dolor sit amet, consectetur adipisicing elit, sed do eiusmod tempor incididunt ut labore et dolore magna aliqua. Ut enim ad minim veniam, quis.</p>
    <p class="tight">Lorem ipsum dolor sit amet, consectetur adipisicing elit, sed do eiusmod tempor incididunt ut labore et dolore magna aliqua. Ut enim ad minim veniam, quis nostrud exercitation ullamco laboris nisi ut aliquip ex ea commodo consequa.Lorem ipsum dolor sit amet, consectetur adipisicing elit, sed do eiusmod tempor incididunt ut labore et dolore magna aliqua. Ut enim ad minim veniam, quis.</p>
    <p>Lorem ipsum dolor sit amet, consectetur adipisicing elit, sed do eiusmod tempor incididunt ut labore et dolore magna aliqua. Ut enim ad minim veniam,</p>
  </div>

  <div class="sign-off">Best regards,<br>Yours Truly,</div>
  <div class="signature">Your Name</div>
  <div class="signatory-role">Company Director</div>
</div>
</body>
</html>
```